Design a Job Application & CV

I need a design for upcoming job applications that includes a cv. It needs to look as elegant and modern as possible as the application will be send mainly to large corporations and strategy consultancies. I have attached an application that I like for your consideration. One of the more difficult requirements is that it needs to be editable in ms office word for mac/windows.
As stated only the design is part of this project. I will fill in my content later on.
Updates
Project Deadline Extended
Reason: Dear Designers,
I am going to increase the budget as well as extending the deadline. I am hoping that you can improve upon the design that I have provided in the brief. If you have questions please let me know.
Dear Designers,
Target Market(s)
Human Resources Managers, Senior Consultants and Executives of larger firms
Industry/Entity Type
Office
Requirements
Must have
- 4 Pages including( a cover page, a coverletter page, 2 pages cv)
It should be easy to edit and should be readable by word for mac, i.e. in the *.docx format.
Here is an example of what I like:
http://www.torvenmaal.de/applicationexample.pdf
http://www.torvenmaal.de/applicationExample.docx
colors that I like are blue, grey, black, white
Nice to have
- icons to indicate sections
Should not have
- invasive cliparts

```html
<!DOCTYPE html>
<html lang="en">
<head>
<meta charset="utf-8">
<title>CV – Experiences</title>
<link href="https://fonts.googleapis.com/css2?family=Dosis:wght@300&family=Libre+Baskerville&display=swap" rel="stylesheet">
<style>
  :root {
    --blue: #1a9ad6;
    --grey: #6d6e71;
    --ink: #1f1f1f;
    --rule: #9a9a9a;
    --paper: #ffffff;
    --edge: #c9c9c9;
  }
  html, body { margin: 0; padding: 0; overflow: hidden; background: var(--paper); }
  .page {
    position: relative;
    width: 848px;
    height: 1200px;
    overflow: hidden;
    background: var(--paper);
    font-family: "Libre Baskerville", Georgia, serif;
    color: var(--ink);
  }
  .page-edge {
    position: absolute;
    left: 0; top: 97px; bottom: 32px;
    width: 1px;
    background: var(--edge);
  }
  .header-bands, .footer-bands { position: absolute; left: 0; display: block; }
  .header-bands { top: 0; }
  .footer-bands { bottom: 0; }
  .page-title {
    position: absolute;
    left: 32px; top: 12px;
    margin: 0;
    font-family: "Dosis", sans-serif;
    font-weight: 300;
    font-size: 56px;
    letter-spacing: 1px;
    color: var(--paper);
  }
  .entry {
    position: absolute;
    left: 34px;
    width: 760px;
    font-size: 15px;
    line-height: 25.6px;
  }
  .entry-period {
    margin: 0;
    padding-bottom: 4px;
    border-bottom: 1.5px dashed var(--rule);
    font-size: 15px;
  }
  .entry-org {
    margin: 9px 0 6px;
    font-size: 16px;
    font-weight: 400;
    letter-spacing: 1.2px;
    text-transform: uppercase;
  }
  .entry-lines { margin: 0; padding: 0; list-style: none; }
</style>
</head>
<body>
<main class="page">
  <svg class="header-bands" width="848" height="97" viewBox="0 0 848 97" aria-hidden="true">
    <polygon points="0,0 630,0 615,97 0,97" fill="var(--blue)"/>
    <polygon points="638,0 848,0 848,97 623,97" fill="var(--grey)"/>
  </svg>
  <h1 class="page-title">Experiences</h1>
  <div class="page-edge"></div>

  <section class="entry" style="top:175px">
    <p class="entry-period">2003 – 2004</p>
    <h2 class="entry-org">Halvern Construction Contractors, Melbourne, Australia</h2>
    <ul class="entry-lines">
      <li>Assistant Engineer</li>
      <li>Secured work experience as an Assistant Engineer reporting directly to the Project Manager.</li>
      <li>Liased with Engineers and reported to Project Manager on all tasks.</li>
      <li>Conducted demolition work which included working with dangerous chemicals such as asbestos.</li>
      <li>Completed survey work using laser instruments.</li>
      <li>Ensured health &amp; safety procedures were adhered to and reported any breaches.</li>
    </ul>
  </section>

  <section class="entry" style="top:451px">
    <p class="entry-period">2002 - 2003</p>
    <h2 class="entry-org">Delmore Electronic Design Services, Cork</h2>
    <ul class="entry-lines">
      <li>Trainee Engineer</li>
      <li>Reported to the Senior Engineer.</li>
      <li>Assisted with designing and building of web pages.</li>
      <li>Liaised with Engineering staff on all aspects of web content relevant to the industry sector.</li>
      <li>Trained on Webline Page Editor for web design.</li>
      <li>Reported on progress at weekly team meetings.</li>
    </ul>
  </section>

  <section class="entry" style="top:730px">
    <p class="entry-period">1999 - 2002</p>
    <h2 class="entry-org">Northgate University College</h2>
    <ul class="entry-lines">
      <li>Information Assistant, Riverside Arena</li>
      <li>Checked membership cards at the information desk.</li>
      <li>Provided assistance and information to customers.</li>
      <li>Collected money for aerobics and yoga classes.</li>
      <li>Managed special group bookings of facilities.</li>
    </ul>
  </section>

  <section class="entry" style="top:970px">
    <p class="entry-period">1993 - 1999</p>
    <h2 class="entry-org">Kestrel Brothers College, Riverside, Cork</h2>
    <ul class="entry-lines">
      <li>Leaving Certificate: 500 Points including an A1 in Physics.</li>
    </ul>
  </section>

  <svg class="footer-bands" width="848" height="32" viewBox="0 0 848 32" aria-hidden="true">
    <polygon points="0,0 209,0 227,32 0,32" fill="var(--grey)"/>
    <polygon points="218,0 848,0 848,32 236,32" fill="var(--blue)"/>
  </svg>
</main>
</body>
</html>
```